Create Lanternfield HR Business Cards.

Create Business Cards for Lanternfield HR. 2 sided and Would like the back to have the logo.

Info for Business Card:
Address: 4827 Millbrook Ave Suite 230 Cleveland, Ohio 44987
Office Number: 216-555-0143
Mobile: 216-555-0192

Website: www.lanternfieldhr.example

Target Market(s)

Small to medium size businesses

Industry/Entity Type

Human Resources

Contact Information for Business Card

Company logo and information

Font styles to use
Serif
Sans Serif

Requirements
Must have
• Info for Business Card: Address: 4827 Millbrook Ave Suite 230 Cleveland, Ohio 44987 Office Number: 216-555-0143 Mobile: 216-555-0192 Website: www.lanternfieldhr.example

```html
<!DOCTYPE html>
<html lang="en">
<head>
<meta charset="utf-8">
<title>Lanternfield HR — Business Cards</title>
<link rel="stylesheet" href="https://fonts.googleapis.com/css2?family=EB+Garamond:wght@400;500&display=swap">
<style>
  :root {
    --navy: #29235c;
    --orange: #f18a25;
    --paper: #ffffff;
    --backdrop: #e4e4e4;
  }
  html, body {
    margin: 0;
    padding: 0;
    width: 1200px;
    height: 960px;
    overflow: hidden;
    background: var(--backdrop);
  }
  .card-sheet {
    display: block;
    width: 1200px;
    height: 960px;
  }
  .contact-text {
    font-family: "EB Garamond", Georgia, serif;
    font-weight: 400;
    fill: var(--navy);
  }
  .contact-text.web { font-size: 17px; }
  .contact-text.line { font-size: 19px; }
  .wordmark {
    font-family: "EB Garamond", Georgia, serif;
    font-weight: 500;
    font-size: 37px;
    text-anchor: middle;
  }
  .front .orbit { fill: none; stroke: var(--navy); stroke-width: 2.2; }
  .front .dot-ring { fill: var(--paper); stroke: var(--navy); stroke-width: 2; }
  .front .dot-core { fill: var(--navy); }
  .front .wordmark { fill: var(--navy); }
  .back .orbit { fill: none; stroke: var(--paper); stroke-width: 2.2; }
  .back .dot-ring { fill: var(--navy); stroke: var(--paper); stroke-width: 2; }
  .back .dot-core { fill: var(--paper); }
  .back .wordmark { fill: var(--paper); }
  .accent-dot { fill: var(--orange); }
  .card-face-front { fill: var(--paper); }
  .card-face-back { fill: var(--navy); }
  .path-guide { fill: none; stroke: none; }
</style>
</head>
<body>
<svg class="card-sheet" viewBox="0 0 1000 800" xmlns="http://www.w3.org/2000/svg">
  <defs>
    <clipPath id="front-clip"><rect x="98" y="82" width="364" height="638"/></clipPath>
    <clipPath id="back-clip"><rect x="540" y="82" width="364" height="638"/></clipPath>

    <!-- text baselines, concentric with the orbits (centre 245,555) -->
    <path id="web-path" class="path-guide" d="M -175 555 A 420 420 0 0 1 665 555"/>
    <path id="mobile-path" class="path-guide" d="M -95 555 A 340 340 0 0 1 585 555"/>
    <path id="office-path" class="path-guide" d="M -20 555 A 265 265 0 0 1 510 555"/>
    <path id="address-path-1" class="path-guide" d="M 56 555 A 189 189 0 0 1 434 555"/>
    <path id="address-path-2" class="path-guide" d="M 87 555 A 158 158 0 0 1 403 555"/>
  </defs>

  <!-- Front: contact details -->
  <g class="front">
    <rect class="card-face-front" x="98" y="82" width="364" height="638"/>
    <g clip-path="url(#front-clip)">
      <circle class="orbit" cx="245" cy="555" r="455"/>
      <circle class="orbit" cx="245" cy="555" r="370"/>
      <circle class="orbit" cx="245" cy="555" r="293"/>
      <circle class="orbit" cx="245" cy="555" r="210"/>
    </g>

    <g class="orbit-dots">
      <circle class="dot-ring" cx="362" cy="118" r="11"/><circle class="dot-core" cx="362" cy="118" r="7"/>
      <circle class="dot-ring" cx="287" cy="184" r="11"/><circle class="dot-core" cx="287" cy="184" r="7"/>
      <circle class="dot-ring" cx="211" cy="265" r="11"/><circle class="dot-core" cx="211" cy="265" r="7"/>
      <circle class="dot-ring" cx="136" cy="376" r="11"/><circle class="dot-core" cx="136" cy="376" r="7"/>
    </g>

    <g clip-path="url(#front-clip)">
      <text class="contact-text web"><textPath href="#web-path" startOffset="553">www.lanternfieldhr.example</textPath></text>
      <text class="contact-text line"><textPath href="#mobile-path" startOffset="488">mobile.</textPath></text>
      <text class="contact-text line"><textPath href="#mobile-path" startOffset="588">216-555-0192</textPath></text>
      <text class="contact-text line"><textPath href="#office-path" startOffset="316">office.</textPath></text>
      <text class="contact-text line"><textPath href="#office-path" startOffset="404">216-555-0143</textPath></text>
      <text class="contact-text line"><textPath href="#address-path-1" startOffset="206">4827 Millbrook Ave Suite 230</textPath></text>
      <text class="contact-text line"><textPath href="#address-path-2" startOffset="176">Cleveland, Ohio 44987</textPath></text>
    </g>

    <g class="brand-lockup">
      <circle class="accent-dot" cx="245" cy="560" r="26"/>
      <text class="wordmark" x="232" y="640">Lanternfield HR</text>
    </g>
  </g>

  <!-- Back: brand side -->
  <g class="back">
    <rect class="card-face-back" x="540" y="82" width="364" height="638"/>
    <g clip-path="url(#back-clip)">
      <circle class="orbit" cx="687" cy="555" r="455"/>
      <circle class="orbit" cx="687" cy="555" r="370"/>
      <circle class="orbit" cx="687" cy="555" r="293"/>
      <circle class="orbit" cx="687" cy="555" r="210"/>
    </g>

    <g class="orbit-dots">
      <circle class="dot-ring" cx="803" cy="120" r="11"/><circle class="dot-core" cx="803" cy="120" r="7"/>
      <circle class="dot-ring" cx="730" cy="185" r="11"/><circle class="dot-core" cx="730" cy="185" r="7"/>
      <circle class="dot-ring" cx="652" cy="266" r="11"/><circle class="dot-core" cx="652" cy="266" r="7"/>
      <circle class="dot-ring" cx="578" cy="376" r="11"/><circle class="dot-core" cx="578" cy="376" r="7"/>
    </g>

    <g class="brand-lockup">
      <circle class="accent-dot" cx="689" cy="536" r="26"/>
      <text class="wordmark" x="676" y="616">Lanternfield HR</text>
    </g>
  </g>
</svg>
</body>
</html>
```